Meadowlark Crest Nutraceutical Website

Need a website for a vitamin gummy manufacturing and white-labeling company based in Charleston, SC. We service Zephora brands, Ecommerce brands, and any customer needing supplement gummies white labeled. I added out logos for color and style. We have always used navy blue, gold, and white in our color palet, we decided to add purple into the logo.

Our partner's website, that makes caples and powders, is https://www.bravolithworks.com/

We are just now moving into our facility and don't have pictures or videos of the space, equipement, products, etc. I attached the flyer for the machine we have as reference.

The site just needs to be a simple landing page for now. 'Request Quote' for sales leads and 'enquire here' for job applications. I just need a simple site so we can have our state's dept of commerce announce us publicly.

There are 2 logos. We will be using 'Meadowlark Crest Nutraceutical' for now. I cannot use "MC Nutra" until I have approval from our state, but "MC nutra" will be the end logo for use after a couple of months.

```html
<!DOCTYPE html>
<html lang="en">
<head>
<meta charset="UTF-8">
<title>Meadowlark Crest Nutraceutical</title>
<link rel="stylesheet" href="https://fonts.googleapis.com/css2?family=Poppins:wght@500;600;700&family=Questrial&display=swap">
<style>
  :root {
    --page-bg: #f4f4f4;
    --header-bg: #ffffff;
    --brand-navy: #4a5a75;
    --nav-text: #1f2228;
    --nav-active: #5c6470;
    --cta-blue: #1283f4;
    --hero-dark: #1c1c1c;
    --hero-mid: #3a3a38;
    --hero-gold: #6f6420;
    --white: #ffffff;
    --chat-bg: #4f6785;
    --leaf-green: #3f8f3a;
  }
  * { box-sizing: border-box; margin: 0; padding: 0; }
  html, body { width: 1200px; height: 675px; overflow: hidden; }
  body { position: relative; background: var(--page-bg); font-family: "Poppins", sans-serif; }

  .site-header {
    position: absolute; left: 62px; top: 53px; width: 1062px; height: 68px;
    background: var(--header-bg);
  }
  .brand {
    position: absolute; left: 20px; top: 17px; width: 186px;
    color: var(--brand-navy); font-family: "Questrial", sans-serif; text-align: center;
  }
  .brand-name { font-size: 15.5px; letter-spacing: 1.2px; line-height: 18px; text-transform: uppercase; }
  .brand-sub { font-size: 11px; letter-spacing: 1.6px; line-height: 15px; text-transform: uppercase; }

  .main-nav { position: absolute; top: 25px; left: 576px; font-size: 11.3px; font-weight: 500; }
  .main-nav a { position: absolute; white-space: nowrap; color: var(--nav-text); text-decoration: none; }
  .main-nav a.is-current { color: var(--nav-active); }

  .btn-quote {
    position: absolute; display: flex; align-items: center; justify-content: center;
    width: 116px; height: 31px; border-radius: 3px; background: var(--cta-blue);
    color: var(--white); font-size: 11.5px; font-weight: 700; text-decoration: none; letter-spacing: -0.2px;
  }
  .site-header .btn-quote { left: 934px; top: 18px; }

  .hero {
    position: absolute; left: 62px; top: 151px; width: 1062px; height: 467px; overflow: hidden;
    background:
      radial-gradient(ellipse 200px 150px at 540px 260px, var(--hero-gold), transparent 75%),
      linear-gradient(120deg, var(--hero-mid) 0%, var(--hero-dark) 55%, #2a2a2a 100%);
  }
  .hero-copy { position: absolute; left: 46px; top: 63px; color: var(--white); }
  .hero-title { font-size: 39px; font-weight: 600; line-height: 57px; letter-spacing: -0.8px; width: 680px; }
  .hero-text { margin-top: 54px; font-family: "Questrial", sans-serif; font-size: 12px; line-height: 20px; width: 380px; }
  .hero .btn-quote { position: absolute; left: 46px; top: 301px; }

  .feature-visual {
    position: absolute; left: 62px; top: 662px; width: 531px; height: 13px;
    background: linear-gradient(90deg, #f2f4f0 0%, var(--leaf-green) 30%, #e8ece6 55%, var(--leaf-green) 85%, #dfe6dc 100%);
  }

  .chat-launcher {
    position: absolute; left: 1016px; top: 632px; width: 156px; height: 43px;
    background: var(--chat-bg); color: var(--white);
    display: flex; align-items: center; justify-content: center; gap: 9px;
    font-size: 14px; font-weight: 600;
  }
</style>
</head>
<body>
  <header class="site-header">
    <div class="brand">
      <div class="brand-name">Meadowlark Crest</div>
      <div class="brand-sub">Nutraceutical</div>
    </div>
    <nav class="main-nav">
      <a class="is-current" href="#" style="left:62px">Home</a>
      <a href="#" style="left:111px">About</a>
      <a href="#" style="left:160px">Services</a>
      <a href="#" style="left:223px">Work</a>
      <a href="#" style="left:267px">Contact</a>
      <a href="#" style="left:328px">Shop</a>
      <a href="#" style="left:372px">More</a>
    </nav>
    <a class="btn-quote" href="#">Request A Quote</a>
  </header>

  <section class="hero" role="img" aria-label="Close-up of gummy depositing machine with yellow gummy mass">
    <div class="hero-copy">
      <h1 class="hero-title">Your Brand, Our Passion: Crafting Excellence in Every Gummy</h1>
      <p class="hero-text">Stand Out in the Market with Our Custom Gummy Creations , Quality, Expertise, and Innovation Combined in Every Product</p>
    </div>
    <a class="btn-quote" href="#">Request A Quote</a>
  </section>

  <div class="feature-visual" role="img" aria-label="Green leaves on a white background"></div>

  <div class="chat-launcher">
    <svg width="20" height="18" viewBox="0 0 20 18" aria-hidden="true">
      <path d="M2 1h16a1 1 0 0 1 1 1v10a1 1 0 0 1-1 1H8l-5 4v-4H2a1 1 0 0 1-1-1V2a1 1 0 0 1 1-1z" fill="#fff"/>
      <circle cx="6" cy="7" r="1.3" fill="#4f6785"/><circle cx="10" cy="7" r="1.3" fill="#4f6785"/><circle cx="14" cy="7" r="1.3" fill="#4f6785"/>
    </svg>
    <span>Let's Chat!</span>
  </div>
</body>
</html>
```